Business Consulting Business Card

professional business card with basic information (1) First and Last name (2) email address, (3) phone number, (4) website.

```html
<!DOCTYPE html>
<html lang="en">
<head>
<meta charset="utf-8">
<title>Tidewell – Business Card</title>
<link rel="stylesheet" href="https://fonts.googleapis.com/css2?family=Montserrat:wght@400;500&family=Arimo:wght@400&display=swap">
<style>
  :root {
    --page-bg: #e9f2f2;
    --card-bg: #ffffff;
    --card-shade: #f1f2f3;
    --ink: #14213a;
    --teal-light: #4fcdc8;
    --teal-deep: #3aa6d2;
    --shadow: rgba(20, 60, 70, 0.14);
  }
  * { box-sizing: border-box; margin: 0; padding: 0; }
  html, body {
    width: 1200px;
    height: 900px;
    overflow: hidden;
    background: var(--page-bg);
  }
  .sheet {
    width: 1200px;
    height: 900px;
    display: flex;
    flex-direction: column;
    align-items: center;
    justify-content: center;
    gap: 60px;
  }
  .card {
    position: relative;
    width: 600px;
    height: 343px;
    background: radial-gradient(circle at 40% 45%, var(--card-bg) 0%, var(--card-shade) 100%);
    box-shadow: 0 10px 30px var(--shadow);
    overflow: hidden;
  }

  /* Front */
  .corner-accent {
    position: absolute;
    top: -120px;
    right: -110px;
    width: 330px;
    height: 330px;
    border-radius: 50%;
    background: linear-gradient(160deg, var(--teal-light), var(--teal-deep));
  }
  .brand {
    position: absolute;
    left: 130px;
    top: 50%;
    transform: translateY(-50%);
    display: flex;
    align-items: center;
    gap: 18px;
  }
  .brand-dot {
    width: 40px;
    height: 40px;
    border-radius: 50%;
    background: linear-gradient(160deg, var(--teal-light), var(--teal-deep));
  }
  .brand-name {
    font-family: "Montserrat", sans-serif;
    font-weight: 400;
    font-size: 30px;
    letter-spacing: 0.32em;
    color: var(--ink);
  }

  /* Back */
  .contact-block {
    position: absolute;
    left: 110px;
    top: 50%;
    transform: translateY(-50%);
    display: flex;
    align-items: center;
    gap: 18px;
  }
  .identity { text-align: right; }
  .person-name {
    font-family: "Arimo", sans-serif;
    font-size: 31px;
    letter-spacing: -0.03em;
    color: var(--ink);
    line-height: 1.05;
  }
  .person-role {
    font-family: "Arimo", sans-serif;
    font-size: 16px;
    color: var(--teal-deep);
    margin-top: 2px;
  }
  .icon-pill {
    width: 40px;
    height: 112px;
    border-radius: 8px;
    background: linear-gradient(180deg, var(--teal-light), var(--teal-deep));
    display: flex;
    flex-direction: column;
    align-items: center;
    justify-content: space-around;
    padding: 10px 0;
  }
  .icon-pill .divider {
    width: 18px;
    height: 2px;
    background: #fff;
  }
  .details {
    font-family: "Arimo", sans-serif;
    font-size: 15px;
    color: var(--ink);
    line-height: 1.25;
    display: flex;
    flex-direction: column;
    gap: 14px;
  }
</style>
</head>
<body>
  <main class="sheet">
    <section class="card card-front" aria-label="Card front">
      <div class="corner-accent"></div>
      <div class="brand">
        <span class="brand-dot"></span>
        <span class="brand-name">TIDEWELL</span>
      </div>
    </section>

    <section class="card card-back" aria-label="Card back">
      <div class="contact-block">
        <div class="identity">
          <p class="person-name">YOUR NAME</p>
          <p class="person-role">Solution Manager</p>
        </div>
        <div class="icon-pill">
          <svg width="18" height="18" viewBox="0 0 24 24" aria-label="Phone">
            <path d="M6.6 10.8a15 15 0 0 0 6.6 6.6l2.2-2.2a1 1 0 0 1 1-.25 11.4 11.4 0 0 0 3.6.57 1 1 0 0 1 1 1V20a1 1 0 0 1-1 1A17 17 0 0 1 3 4a1 1 0 0 1 1-1h3.5a1 1 0 0 1 1 1c0 1.25.2 2.45.57 3.6a1 1 0 0 1-.25 1z" fill="#fff"/>
          </svg>
          <span class="divider"></span>
          <svg width="20" height="20" viewBox="0 0 24 24" aria-label="Website">
            <g fill="none" stroke="#fff" stroke-width="1.8">
              <circle cx="12" cy="12" r="9"/>
              <ellipse cx="12" cy="12" rx="4" ry="9"/>
              <line x1="3" y1="12" x2="21" y2="12"/>
            </g>
          </svg>
        </div>
        <div class="details">
          <div class="phones">
            <p>123-456-7890</p>
            <p>123-456-7890</p>
          </div>
          <div class="web">
            <p>name@email.com</p>
            <p>www.website.com</p>
          </div>
        </div>
      </div>
    </section>
  </main>
</body>
</html>
```